Product label

Create a hip label for a small line of products to be sold at a barbershop.
Updates

Reason: I'm extending the dead line to have improvements made....also since you guys all over the world, I want to accomadet for the day and time differences. Thank you for understanding

Target Market(s)

Men with facial hair....

Industry/Entity Type

Product

Colors

Designer to choose colors to be used in the design.

Requirements
Nice to have
• Nostalgic look, current vibe, easy to read . will need room for ingredients list on the label along with business details...website, no animal testing, made in the USA and shop logo..I'm not apposed to having the logo as a secondary feature on the label as well. Please as creative as you want to be....

```html
<!DOCTYPE html>
<html lang="en">
<head>
<meta charset="utf-8">
<title>Beard Oil Label</title>
<link rel="stylesheet" href="https://fonts.googleapis.com/css2?family=Arimo:wght@400&family=Pirata+One&display=swap">
<style>
  :root {
    --page: #ffffff;
    --label-rust: #9e4a1f;
    --label-ink: #ffffff;
    --frame-line: #f4ece2;
  }
  * { box-sizing: border-box; margin: 0; padding: 0; }
  html, body {
    width: 822px;
    height: 1200px;
    overflow: hidden;
    background: var(--page);
  }
  .canvas {
    position: relative;
    width: 822px;
    height: 1200px;
  }
  .label {
    position: absolute;
    left: 31px;
    top: 433px;
    width: 760px;
    height: 334px;
    background: var(--label-rust);
    color: var(--label-ink);
    font-family: "Arimo", Arial, sans-serif;
  }
  .label-frame {
    position: absolute;
    inset: 0;
    width: 100%;
    height: 100%;
  }
  .info-column {
    position: absolute;
    top: 40px;
    font-size: 15px;
    line-height: 20px;
  }
  .info-column h2 {
    font-size: 15px;
    font-weight: 400;
    margin-bottom: 8px;
  }
  .info-column ul { list-style: none; }
  .info-left { left: 82px; }
  .info-right { left: 540px; }
  .website {
    position: absolute;
    left: 584px;
    top: 244px;
    font-size: 15px;
  }
  .brand {
    position: absolute;
    left: 0;
    right: 0;
    top: 62px;
    display: flex;
    justify-content: center;
    align-items: center;
    gap: 10px;
    font-family: "Pirata One", serif;
    font-size: 30px;
    line-height: 1;
  }
  .brand-dot {
    width: 10px;
    height: 10px;
    border-radius: 50%;
    background: var(--label-ink);
  }
  .product-name {
    position: absolute;
    left: 0;
    right: 0;
    top: 122px;
    text-align: center;
    font-family: "Pirata One", serif;
    font-size: 52px;
    font-weight: 400;
    letter-spacing: 1px;
  }
  .origin {
    position: absolute;
    left: 0;
    right: 0;
    top: 238px;
    text-align: center;
    font-size: 22px;
  }
  .volume {
    position: absolute;
    left: 0;
    right: 0;
    top: 304px;
    text-align: center;
    font-size: 16px;
    line-height: 20px;
  }
</style>
</head>
<body>
<main class="canvas">
  <section class="label">
    <svg class="label-frame" viewBox="0 0 760 334" aria-hidden="true">
      <path d="M48 22 Q30 22 30 42 L30 274 Q30 292 48 292 L712 292 Q730 292 730 274 L730 42 Q730 22 712 22 Z"
            fill="none" stroke="var(--frame-line)" stroke-width="3"/>
      <path d="M30 42 Q14 42 14 28 Q14 14 30 18 M730 42 Q746 42 746 28 Q746 14 730 18
               M30 274 Q14 274 14 286 Q14 298 30 296 M730 274 Q746 274 746 286 Q746 298 730 296"
            fill="none" stroke="var(--frame-line)" stroke-width="3"/>
    </svg>

    <div class="info-column info-left">
      <h2>Business Details</h2>
      <ul>
        <li>xxxxxxxxxxx</li>
        <li>xxxxxxxxxxx</li>
        <li>xxxxxxxxxxx</li>
        <li>xxxxxxxxxxx</li>
        <li>xxxxxxxxxxx</li>
        <li>xxxxxxxxxxx</li>
        <li>xxxxxxxxxxx</li>
        <li>xxxxxxxxxxx</li>
      </ul>
    </div>

    <div class="brand">
      <span class="brand-dot"></span>
      <span class="brand-name">The Copper Comb</span>
    </div>

    <h1 class="product-name">Beard Oil</h1>
    <p class="origin">Made in the USA</p>
    <p class="volume">2oz</p>

    <div class="info-column info-right">
      <h2>No animal testing</h2>
      <ul>
        <li>xxxxxxxxxxx</li>
        <li>xxxxxxxxxxx</li>
        <li>xxxxxxxxxxx</li>
        <li>xxxxxxxxxxx</li>
        <li>xxxxxxxxxxx</li>
        <li>xxxxxxxxxxx</li>
        <li>xxxxxxxxxxx</li>
      </ul>
    </div>
    <p class="website">Website</p>
  </section>
</main>
</body>
</html>
```